Book Cover (QUIET WEEKS MEND EVERY KNOT)

This book is a series of blog posts from my blog, Sparks Kept Handy, which is at glenferrante.example/blog.
The book is to be called:
QUIET WEEKS MEND EVERY KNOT
And 51 other Sparks Kept Handy from the Corner Shop Tutor
(Sparks Kept Handy) should be italicized.
My name is Glen Ferrante, M.B.A.

I will need three variations for my paperback, hardcover and e-book.
Here are some of the blog titles and their topics:
Preparing Your Small Business For Recession small business recession
Should I Incorporate My Business? Should I Incorporate My Business?
Alternative to Minority Shareholder In Small Private Companies minority shareholder
Small Business Culture – Getting it Right Small Business Culture
What is The Right Way to Fire Someone The Right Way to Fire Someone
The Five Basic Leadership Principles Leadership Principles
10 Tips for New Entrepreneurs – Sure Ways to Increase Your Chances of Success
10 things to consider before becoming an entrepreneur
Strategy vs Biz Plans small business strategy
Closing Sales close the sale
Breakeven break even
Growth makes cash flow suck cash flow issues
Think Twice About Offering Early Payment Discounts prepayment discounts
Firing Customers firing customers
Collections best practices getting paid faster
The Cash Flow Statement cash flow statement
Using Paralegals paralegal
Radical Candor radical candor
Why No is the Second Best Word to a Salesperson's ears value of no
The $8 Million Problem -
Contractor vs Employee contractor vs employee
The Columbo sales tactic
Systems Turn Goals From Dreams Into Reality Systems vs Goals
The Importance of Realistic Goals stretch goals
Why The Owner Must Review Every Hire hiring for values
Systems Thinking for Small Biz: The Case for SOPs systems thinking
Trust Your Gut business intuition
Grease and friction grease vs friction
Left alone, 90% of problems solve themselves strategic inaction
Referrals Are Great—But Not a Growth Strategy referrals
The Lean Marketing Machine: 7 Hacks to Grow Your Small Business Fast marketing hacks
The Small Business Health Check small business health check
How to Spot a Customer Headed for Trouble — Before They Take You Down With Them customer warning signs
We Are What We Repeatedly Do habits
The Smartest People Know When to Play Dumb playing dumb
Before You Scale, Do the Math unit economics
AI for Small Business: Practical Tools and Use Cases AI for Small Business
Title: Tell Me Right Now—Why Can’t We Raise Your Prices? small business pricing
Why Your Real Competitor Isn’t Who You Think creative destruction
Good Enough Might Be Great satisficing
Bootstrapping: Building Your Business on Your Terms bootstrapping
Building Resilient Companies That Never Have to Bet the Farm bet the farm
We Always Overshoot: From Fiber to Cannabis to AI AI overbuild
A Bias Toward Action bias toward ation
Choosing the Right Business Owner Title business owner title
Jobs to Be Done: Understanding What Your Customers Really Want Jobs to Be Done
Forget Money. Here’s What Really Motivates People. motivation

Target Market(s)

Small business operators, business school students

Industry/Entity Type

Small business

Colors

Designer to choose colors to be used in the design.

Requirements
Should not have
• Should not look cartoonish

```html
<!DOCTYPE html>
<html lang="en">
<head>
<meta charset="utf-8">
<title>Quiet Weeks Mend Every Knot — Book Cover</title>
<link rel="stylesheet" href="https://fonts.googleapis.com/css2?family=Oswald:wght@500;600;700&display=swap">
<style>
  :root {
    --backdrop: #f1f1f1;
    --cover-yellow: #fbc41a;
    --key-light: #fcd23a;
    --key-mid: #f4b90f;
    --ink: #0c0b08;
    --paper-white: #ffffff;
  }
  * { margin: 0; padding: 0; box-sizing: border-box; }
  html, body {
    width: 1200px;
    height: 1200px;
    overflow: hidden;
    background: var(--backdrop);
  }
  .canvas {
    position: relative;
    width: 1200px;
    height: 1200px;
  }
  .cover {
    position: absolute;
    left: 247px;
    top: 69px;
    width: 707px;
    height: 1061px;
    overflow: hidden;
    background: var(--cover-yellow);
    text-align: center;
    font-family: "Oswald", "Arial Narrow", sans-serif;
    color: var(--ink);
  }
  .title {
    position: absolute;
    top: 36px;
    left: 0;
    right: 0;
    font-weight: 700;
    font-size: 136px;
    line-height: 147px;
    letter-spacing: -2px;
    text-transform: uppercase;
  }
  .title-line {
    display: block;
    transform: scaleX(0.86);
    white-space: nowrap;
  }
  .key-art {
    position: absolute;
    left: 190px;
    top: 638px;
    width: 330px;
    height: 130px;
    border-radius: 65px;
    background: radial-gradient(ellipse at 35% 45%, var(--key-light) 0%, var(--key-mid) 70%, var(--cover-yellow) 100%);
  }
  .subtitle {
    position: absolute;
    top: 800px;
    left: 0;
    right: 0;
    font-weight: 600;
    font-size: 40px;
    line-height: 46px;
    letter-spacing: -0.5px;
    text-transform: uppercase;
    color: var(--paper-white);
    text-shadow:
      -1.5px -1.5px 0 var(--ink), 1.5px -1.5px 0 var(--ink),
      -1.5px 1.5px 0 var(--ink), 1.5px 1.5px 0 var(--ink),
      2px 3px 0 var(--ink);
  }
  .subtitle-line {
    display: block;
    white-space: nowrap;
  }
  .blog-name { font-style: italic; }
  .author {
    position: absolute;
    top: 955px;
    left: 0;
    right: 0;
    font-weight: 600;
    font-size: 62px;
    line-height: 72px;
    letter-spacing: -1px;
    white-space: nowrap;
    transform: scaleX(0.86);
  }
</style>
</head>
<body>
  <main class="canvas">
    <section class="cover">
      <h1 class="title">
        <span class="title-line">Quiet</span>
        <span class="title-line">Weeks</span>
        <span class="title-line">Mend Every</span>
        <span class="title-line">Knot</span>
      </h1>
      <div class="key-art" role="img" aria-label="Yellow key lying flat on a yellow surface"></div>
      <p class="subtitle">
        <span class="subtitle-line">And 51 other <em class="blog-name">Sparks Kept Handy</em></span>
        <span class="subtitle-line">from the Corner Shop Tutor</span>
      </p>
      <p class="author">Glen Ferrante, M.B.A.</p>
    </section>
  </main>
</body>
</html>
```